Business Stationary & Card Design

Double sided business cards, letterhead, horizontal brochure, and envelope design using our logo. We want a modern minimal look. One side of the business card should be only our logo and maybe our slogan "Get It Done Right". The other side should include our coil spring and not the logo again. Watermark like (or not) positioned partially, horizontal, on angle, or a combination of. IF a background color or accent color is used we like blue (4885ed). The letterhead, brochure, and envelope design should be similar to the card. Except no solid background color.Maybe the spring at the bottom of the letterhead page watermark style and partial. Additional info on the business card should be present:
Employee Name
Position
Phone
Email
Address
The final design should communicate strength, simplicity, and newness.

Target Market(s)

35-55 Male & Female

Industry/Entity Type

Automotive

Contact Information for Business Card

One side of the double sided business card should be only our logo and maybe our slogan "Get It Done Right". The other side should include our coil spring and not the logo again. Watermark like (or not) positioned partially, horizontal, on angle, or a combination of. IF a background color or accent color is used we like blue (4885ed). Additional info on the business card should be present:
Employee Name
Position
Phone
Email
Address

Font styles to use
Other font styles liked:
• Use font that compliments the attached font. Maybe plain eurostyle?

Colors
0492cd
3276b5

Requirements
Must have
• Use the coil spring in a subtle unique way (s). Double sided business card
Should not have
• Clutter, colors that do not coordinate well with our logo. Fonts that do not compliment our font.

```html
<!DOCTYPE html>
<html lang="en">
<head>
<meta charset="utf-8">
<title>Torqueline Business Card</title>
<link rel="stylesheet" href="https://fonts.googleapis.com/css2?family=Michroma&family=Work+Sans:wght@400;500&display=swap">
<style>
  :root {
    --bg: #2b2b2b;
    --card: #1b1b1b;
    --accent: #4885ed;
    --accent-deep: #3276b5;
    --accent-bright: #0492cd;
    --ink: #f2f2f2;
    --ink-soft: #d9d9d9;
  }
  * { margin: 0; padding: 0; box-sizing: border-box; }
  html, body { width: 1200px; height: 900px; overflow: hidden; background: var(--bg); }
  .canvas {
    position: relative; width: 1200px; height: 900px;
    display: flex; flex-direction: column; align-items: center; justify-content: center; gap: 40px;
  }
  .card {
    position: relative; width: 700px; height: 400px; background: var(--card);
    box-shadow: 0 10px 30px rgba(0,0,0,.35); overflow: hidden;
  }
  .brand-name {
    font-family: "Michroma", sans-serif; color: var(--accent);
    letter-spacing: 2px; white-space: nowrap; line-height: 1;
    position: absolute; left: 0; right: 0; top: 50%; transform: translateY(-50%);
    text-align: center; font-size: 44px;
  }
  .spring-emblem {
    position: absolute; left: 142px; top: 95px; width: 64px; height: 170px;
    background: linear-gradient(180deg, var(--accent-bright), var(--accent-deep));
    opacity: .85;
  }
  .divider {
    position: absolute; left: 352px; top: 80px; width: 2px; height: 200px; background: var(--accent);
  }
  .contact {
    position: absolute; left: 392px; top: 80px; font-family: "Work Sans", sans-serif; color: var(--ink);
  }
  .contact-name {
    font-family: "Michroma", sans-serif; color: var(--accent); font-size: 20px; letter-spacing: 1px;
  }
  .contact-role { font-size: 16px; color: var(--ink-soft); margin-top: 4px; }
  .contact-address { font-size: 17px; line-height: 1.3; margin-top: 18px; letter-spacing: .5px; }
  .contact-list { list-style: none; margin-top: 10px; font-size: 17px; letter-spacing: .5px; }
  .contact-list li { display: flex; align-items: center; gap: 10px; height: 26px; }
  .contact-list svg { width: 13px; height: 13px; flex: none; }
  .web-highlight { color: var(--accent); }
  .slogan {
    position: absolute; left: 110px; bottom: 48px; font-family: "Michroma", sans-serif;
    color: var(--accent); font-size: 18px; letter-spacing: 1px;
  }
</style>
</head>
<body>
<main class="canvas">
  <section class="card card-front" aria-label="Card front">
    <div class="brand-name">TORQUELINE</div>
  </section>

  <section class="card card-back" aria-label="Card back">
    <div class="spring-emblem" role="img" aria-label="Coil spring emblem"></div>
    <div class="divider"></div>
    <div class="contact">
      <div class="contact-name">DANIEL HARPER</div>
      <div class="contact-role">Director</div>
      <div class="contact-address">418 Alder Avenue Suite 220<br>Riverton, OH 44120</div>
      <ul class="contact-list">
        <li>
          <svg viewBox="0 0 16 16" aria-hidden="true"><path d="M3 1.5l3 .5 1 3.5-2 1.2a9 9 0 0 0 4.3 4.3l1.2-2 3.5 1 .5 3-2 1.5C7 14 2 9 1.5 3.5z" fill="none" stroke="var(--accent)" stroke-width="1.4"/></svg>
          +1 555 0142-7730
        </li>
        <li>
          <svg viewBox="0 0 16 16" aria-hidden="true"><rect x="1" y="3" width="14" height="10" fill="none" stroke="var(--accent)" stroke-width="1.4"/><path d="M1 3l7 6 7-6" fill="none" stroke="var(--accent)" stroke-width="1.4"/></svg>
          info@torqueline.com
        </li>
        <li>
          <svg viewBox="0 0 16 16" aria-hidden="true"><circle cx="8" cy="8" r="6.5" fill="none" stroke="var(--accent)" stroke-width="1.3"/><ellipse cx="8" cy="8" rx="3" ry="6.5" fill="none" stroke="var(--accent)" stroke-width="1.1"/><path d="M1.5 8h13M2.5 5h11M2.5 11h11" stroke="var(--accent)" stroke-width="1"/></svg>
          <span>www.<span class="web-highlight">torqueline</span>.com</span>
        </li>
      </ul>
    </div>
    <div class="slogan">GET IT DONE RIGHT</div>
  </section>
</main>
</body>
</html>
```